Website Design for Varnel Ridge Holdings

I am looking to create a website with 3-4 pages for Varnel Ridge Holdings, a private investment holding company. We already have a logo created via PixelHarbor and would like to incorporate the same dark navy blue color scheme as well as white and potentially other colors including variants of blue, black, and white. We are looking for a conservative, polished design befitting a financial services firm. Our focus as a firm is on identifying opportunities in the overlooked - seeing opportunity where institutional investment is lacking. We are focused on building value for the long-term. We will provide virtually all of the text content but need assistance in setting up the layout, font, design, theme, graphics, etc. The initial three pages will be: Home Page / About Us, "Team", and "Portfolio". Right now, we do not have any portfolio companies but will likely have one within the next several months. The main content page will be the home page. The Team and Portfolio pages will be abbreviated. This website will be expository and is not primarily focused on lead generation or sales.

Ideally, we can incorporate some form of animations / transitions for titles and text sections and stock images (or ideally looped videos) of major city skylines in the U.S. , Latin America, and Europe as those regions are our core investment geographies.

Websites we like that you can use for references include many major private equity firms including Quarrystone Partners (https://www.quarrystonepartners.example/), Brightmoor (https://brightmoor.example/), KLV Holdings (https://www.klvholdings.example/), and Wexholm (https://www.wexholm.example/)
Updates

All,

Thank you to everyone who has posted the initial drafts of the Varnel Ridge Holdings website. The designs are very good. We would now like to review more refined drafts of our website from the designers.

We have posted updated, specific guidance on website page design and text. Please reference the new uploaded "Varnel Ridge Holdings Website Design Guidance" Microsoft Word document to refine your submissions.

Thank you!
Marcus

Target Market(s)

Investment Professionals

Industry/Entity Type

Financial Services

Coding

Coded - Design and coding required

Number of Pages Required

4 page

```html
<!DOCTYPE html>
<html lang="en">
<head>
<meta charset="utf-8">
<title>Varnel Ridge Holdings</title>
<link rel="stylesheet" href="https://fonts.googleapis.com/css2?family=Cormorant+Garamond:wght@300;400;500&family=Urbanist:wght@300;400;500&family=Montserrat:wght@400;500;600&display=swap">
<style>
:root{
  --navy:#0c2340;
  --navy-deep:#0b1a33;
  --ink:#1b1b1b;
  --plum:#231c24;
  --grey-band:#f3f3f3;
  --line:#8a8a8a;
  --white:#ffffff;
  --serif:"Cormorant Garamond", Georgia, serif;
  --display:"Urbanist", "Helvetica Neue", sans-serif;
  --ui:"Montserrat", Arial, sans-serif;
}
*{margin:0;padding:0;box-sizing:border-box}
html,body{width:1200px;height:3856px;overflow:hidden;background:var(--white)}
body{position:relative;font-family:var(--serif);color:var(--ink)}
.abs{position:absolute}
.brand{font-family:var(--ui);font-weight:600;color:var(--navy);font-size:17px;letter-spacing:1.5px;text-transform:uppercase}
.nav a{position:absolute;top:36px;font-family:var(--ui);font-size:12px;font-weight:500;color:var(--ink);text-decoration:none}
.photo{position:absolute}
.notch{position:absolute;background:var(--white)}
.pill{position:absolute;border:1px solid var(--ink);border-radius:20px;font-family:var(--serif);font-size:15px;display:flex;align-items:center;justify-content:center;color:var(--ink)}
.pill.dark{background:#0a0a0a;color:var(--white);border:none;font-size:12px}
.vline{position:absolute;width:1px;background:var(--line)}
.hline{position:absolute;height:1px;background:var(--ink)}
.body-copy{font-size:14.5px;line-height:20.5px}
.label{font-size:13px;color:#555}
.big{font-family:var(--display);font-weight:400}
</style>
</head>
<body>

<header class="site-header">
  <div class="abs brand" style="left:184px;top:33px">Varnel Ridge Holdings</div>
  <nav class="nav">
    <a style="left:558px">Home</a>
    <a style="left:624px">About Us</a>
    <a style="left:712px">Team</a>
    <a style="left:776px">Portfolio</a>
    <a style="left:864px">Contact Us</a>
  </nav>
</header>

<section class="hero">
  <div class="photo" role="img" aria-label="City skyline with tall glass towers under a blue sky" style="left:0;top:85px;width:1200px;height:449px;background:linear-gradient(180deg,#2f7fc4 0%,#5a9fd6 45%,#6d8aa6 70%,#2b3a4d 100%)"></div>
  <div class="notch" style="left:0;top:85px;width:52px;height:39px"></div>
  <h1 class="abs" style="left:175px;top:418px;font-family:var(--serif);font-weight:300;font-size:35px;line-height:35px;color:var(--white)">Varnel Ridge is a leading<br>alternative investment firm.</h1>
  <div class="pill dark" style="left:549px;top:464px;width:117px;height:30px">Get In Touch</div>
</section>

<section class="intro">
  <div class="abs" role="img" aria-label="Faint white geometric cube pattern" style="left:0;top:534px;width:1200px;height:728px;background:linear-gradient(100deg,#e6e6e6 0%,#f6f6f6 30%,#ffffff 55%)"></div>
  <p class="abs body-copy" style="left:251px;top:642px;width:460px">Varnel Ridge Holdings is to have a well-diversified portfolio that efficiently harvests risk premia and protects our capital for future generations. We seek to provide inflation-adjusted returns to preserve the purchasing powers of the assets. We do this via diversification, combining academic theory with our understanding of financial markets, proper risk management and investing for a purpose.</p>
  <div class="pill" style="left:259px;top:799px;width:114px;height:33px">About Us</div>
  <div class="vline" style="left:447px;top:795px;height:365px"></div>
  <div class="abs label" style="left:498px;top:866px">Focus on</div>
  <div class="abs big" style="left:496px;top:888px;font-size:62px;line-height:75px;color:#111">UK, US<br>and<br>Europe</div>
  <div class="photo" role="img" aria-label="Glass office tower seen from below against a cloudy sky" style="left:778px;top:702px;width:370px;height:247px;background:linear-gradient(160deg,#9cc3e6 0%,#3e73aa 45%,#123a66 100%)"></div>
  <div class="notch" style="left:1088px;top:702px;width:60px;height:58px"></div>
  <div class="vline" style="left:778px;top:949px;height:211px"></div>
  <div class="abs label" style="left:834px;top:1042px">Investment Team</div>
  <div class="abs big" style="left:832px;top:1058px;font-size:60px;color:#111">15</div>
</section>

<section class="mission">
  <div class="abs" role="img" aria-label="Faint grey world map" style="left:0;top:1262px;width:1200px;height:492px;background:var(--grey-band)"></div>
  <div class="abs" role="img" aria-label="Blue globe showing the Americas" style="left:153px;top:1384px;width:412px;height:412px;border-radius:50%;background:linear-gradient(135deg,#7fd6f0 0%,#3e8fd2 50%,#1d4f9c 100%)"></div>
  <h2 class="abs big" style="left:257px;top:1340px;font-size:33px;line-height:42.5px;color:#111;width:330px">Our mission is to build and safeguard financial wealth for future generations.</h2>
  <div class="abs" style="left:259px;top:1573px;width:142px;height:3px;background:#111"></div>
  <div class="abs big" style="left:659px;top:1365px;font-size:53px">$50bn</div>
  <div class="abs" style="left:906px;top:1381px;font-size:12px;line-height:12px">Assets under<br>management</div>
  <div class="hline" style="left:609px;top:1434px;width:463px"></div>
  <div class="abs big" style="left:659px;top:1465px;font-size:53px">300+</div>
  <div class="abs" style="left:906px;top:1483px;font-size:12px;line-height:12px">Acquisitions<br>to Date</div>
  <div class="hline" style="left:609px;top:1558px;width:463px"></div>
  <div class="abs big" style="left:665px;top:1575px;font-size:53px">100</div>
  <div class="abs" style="left:906px;top:1610px;font-size:12px">Global staff</div>
</section>

<section class="philosophy">
  <h2 class="abs" style="left:253px;top:1862px;font-family:var(--serif);font-weight:400;font-size:38px;line-height:45px">We believe that when you build differently,<br>you can build better.</h2>
  <div class="vline" style="left:436px;top:1973px;height:175px"></div>
  <p class="abs body-copy" style="left:480px;top:2000px;width:330px">We believe that cooperation and interaction create a strong organization which enables us to deliver results and ultimately generate value for future generations.</p>
  <div class="pill" style="left:477px;top:2096px;width:114px;height:30px">What we do</div>
</section>

<section class="strategy">
  <div class="abs" style="left:0;top:2214px;width:1200px;height:220px;background:var(--plum)"></div>
  <div class="photo" role="img" aria-label="Hand with pen over rising coin stacks, purple tint" style="left:838px;top:2214px;width:362px;height:220px;background:linear-gradient(90deg,var(--plum) 0%,#5d4b68 60%,#7f6a8d 100%)"></div>
  <p class="abs" style="left:262px;top:2270px;width:520px;font-weight:300;font-size:19.5px;line-height:23.5px;color:#e6e0e8">We specialize in private equity and other alternative strategies, investing on behalf of institutional investors around the world. We generate returns by investing in companies across a wide range of industries that need financial and operational support to unlock their full potential.</p>
</section>

<section class="team">
  <div class="photo" role="img" aria-label="Team meeting around a round table in a bright office" style="left:199px;top:2506px;width:469px;height:334px;background:linear-gradient(135deg,#d9d6d2 0%,#a9a49f 50%,#5d5953 100%)"></div>
  <div class="notch" style="left:199px;top:2506px;width:58px;height:54px"></div>
  <div class="hline" style="left:699px;top:2645px;width:241px;background:#777"></div>
  <p class="abs" style="left:708px;top:2668px;width:240px;font-size:14px;line-height:18.3px">Our investment team are held to the standard of treating all of our shareholders, partners, and employees with integrity, respect, and transparency.</p>
  <div class="pill" style="left:705px;top:2778px;width:129px;height:30px">View our team</div>
</section>

<section class="portfolio">
  <div class="abs" style="left:0;top:2921px;width:653px;height:371px;background:var(--navy)"></div>
  <div class="photo" role="img" aria-label="Skyscrapers viewed from street level against a deep blue sky" style="left:653px;top:2921px;width:547px;height:371px;background:linear-gradient(160deg,#2f7be0 0%,#1f5fc4 55%,#3a3430 100%)"></div>
  <div class="notch" style="left:1139px;top:2921px;width:61px;height:55px"></div>
  <p class="abs" style="left:254px;top:3020px;width:330px;font-weight:300;font-size:19.5px;line-height:23.3px;color:#dfe5ee">Varnel Ridge Holdings invest in a wide variety of asset classes: Our portfolio currently spans on Public Equities, Private Equity, Venture Capital, and Real Estate.</p>
  <div class="hline" style="left:254px;top:3250px;width:355px;background:#9aa6b8"></div>
  <div class="abs" style="left:261px;top:3262px;font-size:14px;color:#dfe5ee">View Portfolio</div>
</section>

<section class="newsletter">
  <h2 class="abs" style="left:251px;top:3396px;font-family:var(--serif);font-weight:400;font-size:24px;line-height:30px;color:var(--navy)">Stay in touch with Varnel Ridge<br>Holdings</h2>
  <p class="abs" style="left:609px;top:3398px;width:340px;font-size:12.5px;line-height:17px;color:var(--navy)">To make sure you stay up to date with news about Varnel Ridge Holdings, our partners and portfolio, please fill in the form.</p>
  <div class="abs" style="left:621px;top:3496px;font-size:12px;color:var(--navy)">Enter email</div>
  <div class="hline" style="left:609px;top:3518px;width:336px;background:var(--navy)"></div>
  <div class="pill dark" style="left:606px;top:3540px;width:104px;height:29px">Subscribe</div>
</section>

<footer class="site-footer">
  <div class="abs" style="left:0;top:3663px;width:1200px;height:193px;background:var(--navy-deep)"></div>
  <div class="abs brand" style="left:254px;top:3701px;color:var(--white)">Varnel Ridge Holdings</div>
  <div class="abs" style="left:254px;top:3732px;font-family:var(--ui);font-size:8.5px;color:var(--white)">Copyright © 2025 Varnel Ridge Holdings</div>
  <div class="abs" style="left:757px;top:3829px;font-family:var(--ui);font-size:8.5px;color:var(--white)">Terms of Use &amp; Disclaimers</div>
  <div class="abs" style="left:889px;top:3829px;font-family:var(--ui);font-size:8.5px;color:var(--white)">Privacy Policy</div>
</footer>

</body>
</html>
```